Careers banner for Aluminium Extrusion Company

We are looking to create a Careers banner for our new web site, we are an Aluminium Extrusion business that has careers in technical design, engineering and manufacturing. We are looking to attract both graduates and non graduates. I have attached the current banner for a feel of the colour scheme.

Target Market(s)

Job Hunters

Industry/Entity Type

Manufacturer

Colors

Designer to choose colors to be used in the design.

```html
<!DOCTYPE html>
<html lang="en">
<head>
<meta charset="UTF-8">
<title>Careers – Korval Group</title>
<link rel="stylesheet" href="https://fonts.googleapis.com/css2?family=Questrial&display=swap">
<style>
  :root {
    --bg: #000000;
    --frame: #d9d9d9;
    --text-main: #e6e6e6;
    --text-soft: #c8c8c8;
    --accent-green: #12b81f;
    --accent-glow: rgba(30, 230, 60, 0.45);
    --brand-blue: #2a8fd6;
    --photo-light: #8a8a8a;
    --photo-mid: #3c3c3c;
    --photo-dark: #101010;
  }
  html, body {
    margin: 0;
    padding: 0;
    overflow: hidden;
    background: var(--bg);
  }
  .banner {
    position: relative;
    width: 1200px;
    height: 398px;
    background: var(--bg);
    overflow: hidden;
    font-family: "Questrial", Arial, sans-serif;
  }
  .banner__frame {
    position: absolute;
    inset: 12px;
    border: 1px solid var(--frame);
    pointer-events: none;
    z-index: 5;
  }
  .team-photo {
    position: absolute;
    top: 13px;
    right: 13px;
    width: 560px;
    height: 372px;
    background:
      linear-gradient(90deg, var(--bg) 0%, rgba(0,0,0,0.75) 18%, rgba(0,0,0,0) 45%),
      radial-gradient(ellipse 60% 75% at 68% 60%, var(--photo-light) 0%, var(--photo-mid) 50%, var(--photo-dark) 100%);
  }
  .headline {
    position: absolute;
    left: 40px;
    top: 70px;
    margin: 0;
    font-size: 29px;
    font-weight: 400;
    line-height: 42px;
    color: var(--text-main);
    z-index: 2;
  }
  .contact {
    position: absolute;
    left: 40px;
    top: 203px;
    z-index: 2;
  }
  .contact__label {
    margin: 0;
    font-size: 14px;
    color: var(--text-soft);
  }
  .contact__email {
    display: block;
    margin-top: 4px;
    font-size: 18px;
    color: var(--text-main);
    text-decoration: none;
  }
  .cta {
    position: absolute;
    left: 489px;
    top: 235px;
    width: 178px;
    height: 51px;
    display: flex;
    align-items: center;
    justify-content: center;
    background: var(--accent-green);
    color: #ffffff;
    font-size: 26px;
    text-decoration: none;
    box-shadow: 0 0 40px 12px var(--accent-glow);
    z-index: 3;
  }
  .brand {
    position: absolute;
    left: 104px;
    top: 300px;
    display: flex;
    align-items: center;
    gap: 10px;
    z-index: 2;
  }
  .brand__dot {
    width: 36px;
    height: 36px;
    border-radius: 50%;
    background: var(--brand-blue);
  }
  .brand__name {
    font-size: 22px;
    color: #ffffff;
    letter-spacing: 0.5px;
  }
</style>
</head>
<body>
  <section class="banner">
    <div class="team-photo" role="img" aria-label="Black and white photo of a smiling team of young professionals in business attire in front of large machine gears"></div>

    <h1 class="headline">Would you share your knowledge<br>and talents to strengthen our team?</h1>

    <div class="contact">
      <p class="contact__label">Send your resume to:</p>
      <a class="contact__email" href="mailto:careers@korvalgroup.com">careers@korvalgroup.com</a>
    </div>

    <a class="cta" href="#join">Join now!</a>

    <div class="brand">
      <span class="brand__dot"></span>
      <span class="brand__name">KORVAL GROUP</span>
    </div>

    <div class="banner__frame"></div>
  </section>
</body>
</html>
```